Family Ranch with a hobby vineyard needs 2 wine labels for our first harvest

Design 2 wine labels (front and back) with the Brindor Ranch logo.
Label 1:
Sauvignon Blanc
Alc. 12.5% by Vol.
Palos Verdes Peninsula - add as the region
Year 2022
Label 2:
Cabernet Sauvignon
Alc. 13.5% by Vol.
Year 2022
For the back label design:
GOVERNMENT WARNING: (1) According to the Surgeon General, women
should not drink alcoholic beverages during pregnancy because of the risk of
birth defects. (2) Consumption of alcoholic beverages impairs your ability to
drive a car or operate machinery, and may cause health problems.
Contains Sulfates.
750ML
I just received the bottles and have attached a picture.
Look and feel
Each slider illustrates characteristics of the customer's brand and the style your logo design should communicate.

```html
<!DOCTYPE html>
<html lang="en">
<head>
<meta charset="utf-8">
<title>Brindor Ranch Wine Labels</title>
<link rel="stylesheet" href="https://fonts.googleapis.com/css2?family=Zilla+Slab:wght@700&family=Roboto+Condensed:wght@300&family=Archivo:wght@400;700;800&family=Arimo:wght@400;700&display=swap">
<style>
  :root {
    --backdrop: #e3e4e6;
    --label-white: #ffffff;
    --ink: #1d1d1f;
    --gold: #b88a2e;
    --engraving-light: #eceded;
    --engraving-dark: #b9bbbe;
    --blanc-accent: #e63a24;
    --cabernet-accent: #f5c80f;
  }
  * { margin: 0; padding: 0; box-sizing: border-box; }
  html, body { width: 1200px; height: 2700px; overflow: hidden; }
  body { background: var(--backdrop); font-family: "Archivo", sans-serif; color: var(--ink); }

  .wine-set { position: relative; width: 1200px; height: 1350px; }

  .label {
    position: absolute;
    background: var(--label-white);
    overflow: hidden;
    border-radius: 50% 50% 14px 14px / 40px 40px 14px 14px;
    box-shadow: 0 6px 22px rgba(0,0,0,0.08);
  }
  .front-label { left: 70px; top: 365px; width: 520px; height: 620px; }
  .back-label  { left: 630px; top: 525px; width: 500px; height: 300px; }

  .brand { position: absolute; top: 62px; left: 0; right: 0; display: flex; align-items: center; justify-content: center; gap: 14px; }
  .brand-dot { width: 30px; height: 30px; border-radius: 50%; background: var(--gold); }
  .brand-name { font-family: "Archivo", sans-serif; font-weight: 700; font-size: 36px; letter-spacing: 1px; color: var(--ink); text-transform: uppercase; }

  .vineyard-scene {
    position: absolute; left: 0; right: 0; top: 200px; height: 175px;
    background: linear-gradient(180deg, var(--engraving-light) 0%, #d4d5d7 45%, var(--engraving-dark) 100%);
  }

  .alcohol {
    position: absolute; left: 58px; top: 405px;
    writing-mode: vertical-rl;
    font-family: "Arimo", sans-serif; font-size: 15px; letter-spacing: 0.5px;
  }
  .divider { position: absolute; left: 100px; top: 405px; width: 2px; height: 170px; background: var(--ink); }

  .wine-details { position: absolute; left: 125px; top: 400px; }
  .varietal { font-family: "Zilla Slab", serif; font-weight: 700; font-size: 40px; line-height: 40px; color: var(--gold); letter-spacing: 1.5px; text-transform: uppercase; }
  .vintage { margin-top: 28px; font-family: "Roboto Condensed", sans-serif; font-weight: 300; font-size: 30px; }
  .region { margin-top: 20px; font-weight: 800; font-size: 17px; letter-spacing: 1.2px; text-transform: uppercase; }

  .corner { position: absolute; bottom: 0; width: 70px; height: 70px; }
  .front-label .corner { right: 0; clip-path: polygon(100% 0, 100% 100%, 0 100%); }
  .back-label .corner { left: 0; width: 85px; height: 85px; clip-path: polygon(0 0, 100% 100%, 0 100%); }
  .blanc .corner { background: var(--blanc-accent); }
  .cabernet .corner { background: var(--cabernet-accent); }

  .warning {
    position: absolute; left: 70px; right: 55px; top: 72px;
    font-family: "Arimo", sans-serif; font-size: 13.5px; line-height: 17px;
    text-align: justify; text-align-last: center;
  }
  .warning strong { font-weight: 700; }
  .sulfates, .volume { position: absolute; left: 0; right: 0; text-align: center; font-family: "Arimo", sans-serif; font-size: 14px; }
  .sulfates { top: 190px; }
  .volume { top: 225px; }
</style>
</head>
<body>

<section class="wine-set blanc">
  <article class="label front-label">
    <div class="brand"><span class="brand-dot"></span><span class="brand-name">Brindor Ranch</span></div>
    <div class="vineyard-scene" role="img" aria-label="Engraved sketch of rolling hills and vineyard rows"></div>
    <div class="alcohol">ALC. 12.5%/VOL</div>
    <div class="divider"></div>
    <div class="wine-details">
      <h2 class="varietal">Sauvignon<br>Blanc</h2>
      <p class="vintage">— 2022</p>
      <p class="region">Palos Verdes Peninsula</p>
    </div>
    <div class="corner"></div>
  </article>

  <article class="label back-label">
    <p class="warning"><strong>GOVERNMENT WARNING:</strong> (1) According to the Surgeon General, women should not drink alcoholic beverages during pregnancy because of the risk of birth defects. (2) Consumption of alcoholic beverages impairs your ability to drive a car or operate machinery, and may cause health problems.</p>
    <p class="sulfates">Contains Sulfates</p>
    <p class="volume">750ML</p>
    <div class="corner"></div>
  </article>
</section>

<section class="wine-set cabernet">
  <article class="label front-label">
    <div class="brand"><span class="brand-dot"></span><span class="brand-name">Brindor Ranch</span></div>
    <div class="vineyard-scene" role="img" aria-label="Engraved sketch of rolling hills and vineyard rows"></div>
    <div class="alcohol">ALC. 13.5%/VOL</div>
    <div class="divider"></div>
    <div class="wine-details">
      <h2 class="varietal">Cabernet<br>Sauvignon</h2>
      <p class="vintage">— 2022</p>
      <p class="region">Palos Verdes Peninsula</p>
    </div>
    <div class="corner"></div>
  </article>

  <article class="label back-label">
    <p class="warning"><strong>GOVERNMENT WARNING:</strong> (1) According to the Surgeon General, women should not drink alcoholic beverages during pregnancy because of the risk of birth defects. (2) Consumption of alcoholic beverages impairs your ability to drive a car or operate machinery, and may cause health problems.</p>
    <p class="sulfates">Contains Sulfates</p>
    <p class="volume">750ML</p>
    <div class="corner"></div>
  </article>
</section>

</body>
</html>
```